Koruvo Martial Art Website Redesign

We have an existing website at www.koruvo.com.au and are looking for a fresh new design for it as it's looking old and cluttered.

When doing the social media icons, we also need one for Vid Stream which we currently don't have on the site.

We are happy with the actual copy and just want a redesign.

It needs to look dark and edgy.

Target Market(s)

People interested in self defence classes and private training

Number of Pages Required

1 page

Font styles to use
Sans Serif

```html
<!DOCTYPE html>
<html lang="en">
<head>
<meta charset="utf-8">
<title>Koruvo Martial Art</title>
<link href="https://fonts.googleapis.com/css2?family=Poppins:wght@500;600;700&family=Open+Sans:wght@400;600;700&display=swap" rel="stylesheet">
<style>
:root{
  --page:#ffffff;
  --black:#0b0b0b;
  --dark:#141414;
  --navy:#0a1626;
  --navy-deep:#061020;
  --red:#e8302a;
  --gold:#f5c518;
  --gold-dark:#9a7a12;
  --text:#e6e6e6;
  --muted:#9aa0a8;
  --field:#ffffff;
}
*{box-sizing:border-box;margin:0;padding:0}
html,body{width:1200px;height:4699px;overflow:hidden;background:var(--page)}
body{position:relative;font-family:"Open Sans",sans-serif;color:var(--text)}
.site{position:absolute;left:123px;top:140px;width:950px;height:4393px;background:var(--black);overflow:hidden;box-shadow:0 6px 24px rgba(0,0,0,.35)}
.abs{position:absolute}
.bg{position:absolute;left:0;top:0}
.photo{position:absolute;z-index:0}
.h2{position:absolute;left:0;width:950px;text-align:center;font-family:"Poppins",sans-serif;font-weight:700;font-size:21px;letter-spacing:.5px;color:#fff}
.h2::after{content:"";display:block;width:100px;height:3px;margin:6px auto 0;background:linear-gradient(90deg,var(--red),var(--gold))}
.h2,.abs,.card-label,.hero-title,.btn,.field,.quote,.arrow,.logo,.ribbon,.else-title,.social{z-index:2}
.p{font-size:10.5px;line-height:16.5px;color:var(--text)}
.p + .p{margin-top:12px}
/* nav */
.topbar{position:absolute;left:0;top:0;width:950px;height:56px;background:var(--dark);box-shadow:0 3px 8px rgba(0,0,0,.5);z-index:3}
.logo{position:absolute;display:flex;align-items:center;gap:6px;font-family:"Open Sans",sans-serif;font-weight:600;font-size:11px;color:#fff}
.logo i{display:block;width:28px;height:28px;border-radius:50%;background:var(--gold)}
.nav a,.subnav a{position:absolute;font-family:"Poppins",sans-serif;font-style:italic;font-weight:600;font-size:10px;color:#fff;text-decoration:none;white-space:nowrap}
.nav a.active{color:var(--red)}
.nav a.active::after{content:"";position:absolute;left:0;right:0;top:17px;height:2px;background:var(--red)}
.subnav{position:absolute;left:0;top:56px;width:950px;height:55px;background:#1a1a1a;z-index:3}
.caret{display:inline-block;width:0;height:0;border-left:5px solid transparent;border-right:5px solid transparent;border-top:6px solid #fff;margin-left:8px;vertical-align:1px}
/* hero */
.ribbon{position:absolute;left:13px;top:160px;height:26px;width:136px;background:var(--gold);clip-path:polygon(0 0,100% 0,88% 50%,100% 100%,0 100%);font-family:"Poppins",sans-serif;font-style:italic;font-weight:600;font-size:9.5px;color:#111;line-height:26px;padding-left:10px}
.hero-title{position:absolute;left:67px;top:306px;font-family:"Poppins",sans-serif;font-weight:700;font-size:31px;line-height:47px;color:var(--red);letter-spacing:.5px}
.btn{position:absolute;display:block;font-family:"Poppins",sans-serif;font-style:italic;font-weight:600;text-align:center;text-decoration:none}
.btn-red{background:var(--red);color:#fff;font-size:10px}
.btn-gold{background:var(--gold);color:#111;font-size:10px}
.hl-gold{color:var(--gold);font-weight:700}
.hl-red{color:var(--red);font-weight:700}
/* services */
.card-label{position:absolute;font-family:"Poppins",sans-serif;font-weight:600;font-size:10px;line-height:16px;color:#fff;width:227px}
/* feedback */
.quote{position:absolute;font-family:"Poppins",sans-serif;font-weight:700;font-size:70px;line-height:70px;color:var(--gold)}
.arrow{position:absolute;font-family:"Poppins",sans-serif;font-size:42px;color:var(--red)}
/* form */
.field{position:absolute;height:29px;background:var(--field);border:none;font-family:"Open Sans",sans-serif;font-size:10px;color:#aaa;padding:8px 9px}
/* what else */
.else-title{position:absolute;font-family:"Poppins",sans-serif;font-weight:700;font-size:15px;line-height:17px;color:var(--gold)}
.footer-links a{display:block;font-size:9.5px;line-height:23px;color:var(--muted);text-decoration:none}
.social{position:absolute;display:flex;gap:12px}
.social span{display:block;width:14px;height:14px;border:2px solid var(--muted);border-radius:3px}
</style>
</head>
<body>
<main class="site">

  <svg class="bg" width="950" height="4393" viewBox="0 0 950 4393" aria-hidden="true">
    <rect width="950" height="4393" fill="#0b0b0b"/>
    <polygon points="0,305 0,595 270,550" fill="#c9a318"/>
    <polygon points="0,430 0,595 270,550" fill="#8a6f10" opacity=".55"/>
    <polygon points="270,550 950,420 950,550 0,620 0,595" fill="#0b0b0b"/>
    <polygon points="0,1376 475,1452 0,1530" fill="#a3221f"/>
    <polygon points="0,1376 475,1452 330,1430" fill="#c9a318" opacity=".6"/>
    <polygon points="475,1452 950,1370 950,2111 0,2111 0,1530" fill="#081423"/>
    <rect x="0" y="2111" width="950" height="470" fill="#0a0f18"/>
    <rect x="0" y="2580" width="950" height="530" fill="#0b0b0b"/>
    <polygon points="0,3110 950,3110 950,3960 0,4120" fill="#081423"/>
    <polygon points="0,4120 950,3960 950,4180 0,4180" fill="#0b0b0b"/>
    <polygon points="560,4060 950,3962 950,4125" fill="#b4921a"/>
    <rect x="0" y="4180" width="950" height="213" fill="#0b0b0b"/>
  </svg>

  <header class="topbar">
    <div class="logo" style="left:69px;top:14px"><i></i>Koruvo Martial Art</div>
    <nav class="nav">
      <a class="active" href="#" style="left:449px;top:22px">HOME</a>
      <a href="#" style="left:542px;top:22px">COMMUNITY</a>
      <a href="#" style="left:635px;top:22px">BLOG</a>
      <a href="#" style="left:730px;top:22px">MERCHANDISE</a>
      <a href="#" style="left:848px;top:22px">CONTACT US</a>
    </nav>
  </header>
  <nav class="subnav">
    <a href="#" style="left:120px;top:20px">ABOUT THE ART<span class="caret"></span></a>
    <a href="#" style="left:268px;top:20px">TRAINING OPTION<span class="caret"></span></a>
    <a href="#" style="left:428px;top:20px">TRAINING LOCATION<span class="caret"></span></a>
    <a href="#" style="left:603px;top:20px">OUR INSTRUCTORS<span class="caret"></span></a>
    <a href="#" style="left:767px;top:20px">GALLERY<span class="caret"></span></a>
  </nav>

  <section class="hero">
    <div class="photo" role="img" aria-label="Martial arts instructor in a dark uniform, moody black and white portrait" style="left:330px;top:111px;width:460px;height:380px;background:radial-gradient(ellipse at 50% 40%,#4a4a4a 0%,#262626 55%,rgba(20,20,20,0) 80%)"></div>
    <div class="ribbon">WE ARE STILL OPEN</div>
    <h1 class="hero-title">Learn fast, Powerful ‘Street’<br>Self-Defence</h1>
    <a class="btn btn-red" href="#" style="left:67px;top:425px;width:136px;height:35px;line-height:35px">REGISTER NOW</a>
  </section>

  <section class="who">
    <div class="photo" role="img" aria-label="Two instructors in black shirts demonstrating a gun disarm" style="left:520px;top:613px;width:420px;height:363px;background:radial-gradient(ellipse at 55% 45%,#3a3a3a 0%,#1c1c1c 60%,rgba(11,11,11,0) 85%)"></div>
    <h2 class="h2" style="top:663px;left:-25px">WHO WE ARE</h2>
    <div class="abs" style="left:100px;top:732px;width:20px;height:222px;background:linear-gradient(180deg,rgba(163,34,31,0),rgba(163,34,31,.6))"></div>
    <div class="abs" style="left:120px;top:740px;width:345px">
      <p class="p">Koruvo Martial Art® is a fast, powerful, dynamic and ‘street’ effective self-defence style that teaches efficient, practical and easily adaptable techniques for the modern world.</p>
      <p class="p">We believe everyone has the right to feel safe. We understand that we live in a society where it’s become vital to be able to effectively <span class="hl-gold">protect ourselves</span> and <span class="hl-red">loved ones</span> and we will teach you the techniques, strategies and mind-set to effectively and efficiently take control of any street situation quickly.</p>
      <p class="p">Koruvo Martial Art® was created for the ‘real world’. Our focus is on fast, powerful, practical and adaptable street self-defence techniques.</p>
    </div>

    <div class="photo" role="img" aria-label="Two instructors demonstrating a knife defence" style="left:76px;top:1004px;width:345px;height:363px;background:radial-gradient(ellipse at 50% 45%,#3a3a3a 0%,#1c1c1c 60%,rgba(11,11,11,0) 85%)"></div>
    <div class="abs" style="left:458px;top:1230px;width:20px;height:130px;background:linear-gradient(180deg,rgba(201,163,24,0),rgba(201,163,24,.55))"></div>
    <div class="abs" style="left:481px;top:1113px;width:350px">
      <p class="p">Koruvo Martial Art® stemmed from a traditional Burmese martial art and Master Daniel Voss (Ne Aung Lwin) has direct lineage to this traditional art form.</p>
      <p class="p">Over his lifetime, Master Voss has adapted this traditional style to suit today’s urban environment and created a fast and effective self-protection style suited for the modern world in which we live in.</p>
      <p class="p">Koruvo Martial Art® is not just about kicking or striking, it goes beyond the physical. Not only do you learn practical self-defence skills; you will develop a greater sense of empowerment, confidence and focus and awareness, which will have a flow on effect in your daily life.</p>
    </div>
  </section>

  <section class="services">
    <h2 class="h2" style="top:1523px">WHAT WE DO</h2>
    <div class="photo" role="img" aria-label="Two people grappling in a private training session" style="left:120px;top:1597px;width:227px;height:149px;background:linear-gradient(180deg,#e8e6e2,#a9a6a0)"></div>
    <div class="photo" role="img" aria-label="Group training outdoors in a park" style="left:360px;top:1597px;width:227px;height:149px;background:linear-gradient(180deg,#8aa0a8,#4f5b47)"></div>
    <div class="photo" role="img" aria-label="Small group class on the beach" style="left:601px;top:1597px;width:228px;height:149px;background:linear-gradient(180deg,#9fb0c4,#c9cfd6)"></div>
    <p class="card-label" style="left:120px;top:1756px">ONE-ON-ONE PRIVATE TRAINING</p>
    <p class="card-label" style="left:360px;top:1756px">TRAINING CONDUCTED OUTDOORS IN FRESH AIR</p>
    <p class="card-label" style="left:601px;top:1756px">SMALLER GROUP CLASSES</p>

    <div class="photo" role="img" aria-label="Hands using a hand sanitiser pump" style="left:120px;top:1817px;width:227px;height:149px;background:linear-gradient(135deg,#e9e3dd,#c8b7a8)"></div>
    <div class="photo" role="img" aria-label="Person on a yoga mat following an online lesson on a laptop" style="left:360px;top:1817px;width:227px;height:149px;background:linear-gradient(180deg,#f4f2ee,#5e8fd0)"></div>
    <div class="photo" role="img" aria-label="Runner silhouetted against a golden sunset" style="left:601px;top:1817px;width:228px;height:149px;background:linear-gradient(180deg,#d99a2b,#7a4a10)"></div>
    <p class="card-label" style="left:120px;top:1976px">INCREASED HYGIENE MEASURES</p>
    <p class="card-label" style="left:360px;top:1976px">CALLLINK/ONLINE LESSONS AVAILABLE</p>
    <p class="card-label" style="left:601px;top:1976px">STAY HEALTHY AND ACTIVE!</p>
  </section>

  <section class="feedback">
    <h2 class="h2" style="top:2142px">FEEDBACK</h2>
    <span class="arrow" style="left:120px;top:2278px;color:#555">‹</span>
    <span class="arrow" style="left:810px;top:2278px">›</span>
    <span class="quote" style="left:204px;top:2205px">“</span>
    <p class="abs" style="left:279px;top:2219px;font-family:'Poppins',sans-serif;font-weight:600;font-size:10.5px;color:var(--gold)">Martin Hale</p>
    <p class="p abs" style="left:279px;top:2250px;width:390px">I attended a work function. I left to head home to my wife and our new baby and for no reason I was jumped on from behind. I dropped this attacker as well as two of his friends who started throwing punches at me. Thanks to Koruvo Martial Art and my instructor for teaching me the necessary skills, and for giving me the confidence to handle these guys, and to get me home safely to my family.</p>
    <div class="abs" style="left:697px;top:2202px;width:2px;height:172px;background:var(--gold)"></div>
    <div class="abs" style="left:403px;top:2372px;width:296px;height:2px;background:var(--gold)"></div>
    <span class="quote" style="left:697px;top:2378px">”</span>
    <div class="photo" role="img" aria-label="Close-up of hands tying a black belt embroidered with lettering" style="left:276px;top:2383px;width:400px;height:160px;border-radius:0 0 50% 50%/0 0 60% 60%;background:linear-gradient(180deg,#3a3a3a,#1a1a1a)"></div>
  </section>

  <section class="register">
    <h2 class="h2" style="top:2600px">REGISTER NOW</h2>
    <div class="field" style="left:279px;top:2677px;width:227px">Name*</div>
    <div class="field" style="left:521px;top:2677px;width:147px">Age*</div>
    <div class="field" style="left:279px;top:2717px;width:227px">Email*</div>
    <div class="field" style="left:279px;top:2759px;width:227px">Phone</div>
    <div class="field" style="left:279px;top:2799px;width:227px">Mobile*</div>
    <div class="field" style="left:279px;top:2840px;width:227px">Suburb*</div>
    <div class="field" style="left:521px;top:2840px;width:147px">State*</div>
    <div class="field" style="left:279px;top:2880px;width:227px">Previous martial art experience*</div>
    <div class="field" style="left:279px;top:2920px;width:389px;height:98px">Additional comments</div>
    <a class="btn btn-gold" href="#" style="left:563px;top:3040px;width:105px;height:31px;line-height:31px">CONTINUE</a>
  </section>

  <section class="more">
    <h2 class="h2" style="top:3186px;left:-13px">WHAT ELSE</h2>
    <h3 class="else-title" style="left:120px;top:3261px;width:340px">New training options available via CallLink, MeetRoom and FaceChat</h3>
    <div class="abs" style="left:120px;top:3308px;width:350px">
      <p class="p">When ‘life happens’, it is an opportunity to rise up and show our strength and courage. With the recent pandemic hitting our shores, it meant some changes needed to happen with training, whilst conforming with the strict government regulations and hygiene protocols.</p>
      <p class="p" style="margin-top:16px">With our wellbeing and health being highlighted and taking precedence in most people’s lives, we felt it more important than ever before to help keep our members training. Numerous studies have shown that physical activity is linked to boosting our immune system as well as maintain physical and mental wellbeing.</p>
    </div>
    <a class="btn btn-gold" href="#" style="left:120px;top:3529px;width:105px;height:29px;line-height:29px">READ MORE</a>
    <div class="photo" role="img" aria-label="Laptop on a desk among plants showing an online sparring lesson" style="left:524px;top:3254px;width:305px;height:242px;background:linear-gradient(135deg,#6a7a52,#2f3a2a 60%,#c7c2b8)"></div>

    <div class="photo" role="img" aria-label="Woman stretching on a yoga mat at home" style="left:120px;top:3625px;width:308px;height:241px;background:linear-gradient(135deg,#7d8a54,#c9b78f 60%,#b5523a)"></div>
    <h3 class="else-title" style="left:481px;top:3632px;width:350px">Mental Wellbeing and Support During the Global Pandemic</h3>
    <p class="p abs" style="left:481px;top:3681px;width:350px">As global citizens, we have all been adversely affected by the COVID-19 Pandemic. This might just be to our day-to-day socio-occupational routines and training regimes but most likely than not, it has affected our sense of security and certainty about the future to some extent. For some, it can be hard not to worry what the Pandemic and its socio-economic impacts can mean for ourselves, our families, friends and communities.</p>
    <a class="btn btn-gold" href="#" style="left:481px;top:3817px;width:107px;height:29px;line-height:29px">READ MORE</a>
  </section>

  <section class="newsletter">
    <h2 class="abs" style="left:0;width:950px;top:4029px;text-align:center;font-family:'Poppins',sans-serif;font-weight:700;font-size:15px;line-height:24px;color:#fff">Subscribe to our<br>E-newsletter</h2>
    <div class="field" style="left:200px;top:4097px;width:187px">Name</div>
    <div class="field" style="left:401px;top:4097px;width:187px">Email</div>
    <a class="btn btn-gold" href="#" style="left:601px;top:4097px;width:107px;height:29px;line-height:29px">SUBSCRIBE</a>
  </section>

  <footer>
    <div class="logo" style="left:69px;top:4257px"><i></i>Koruvo Martial Art</div>
    <div class="footer-links abs" style="left:225px;top:4252px">
      <a href="#">Home</a>
      <a href="#">Privacy Policy</a>
      <a href="#">Terms and Conditions</a>
    </div>
    <div class="social" style="left:760px;top:4256px">
      <span aria-label="Vid Stream"></span><span aria-label="Photo sharing"></span><span aria-label="Social network"></span><span aria-label="Professional network"></span><span aria-label="Microblog"></span>
    </div>
    <p class="abs" style="left:0;width:950px;top:4364px;text-align:center;font-size:8.5px;color:var(--muted)">© 2021 Koruvo Martial Art</p>
  </footer>
</main>
</body>
</html>
```